Diverse, up-scale salon needs eye-catching, unique business cards.

We are looking for a unique business card design for our stylist but that can also be multi functional and used for appointment reminder and referrals. I will need a design in a format that I can modify names and titles going forward. In the past we have had a dark background with the logo on one side, and stylist and contact information on the other but we are open to all ideas. I have included our mission statement as well as branded colors below. The statement doesn't need to go on the card, it's just a reference for target market. We need space for the stylists name, title, instagram handle and then the salons phone number, website and address. I am also open to adding a spot for a qr code linked to the stylist instagram or the salon booking link.

primary brand colors:
#333333 #233415 #36502a #93874a #000000
Mission statement:
Morvane Hair Studio, a high-end salon located in the lively Downtown Farmington, Michigan, is committed to providing exceptional services in a welcoming and relaxed environment to meet the needs of our diverse clientele.
Our salon specializes in contemporary custom haircuts, coloring, extensions, and barbering and beard grooming services. Our team of skilled stylists is passionate and inventive in their hair styling techniques. At the heart of our salon are values centered on quality, innovation, creativity, and above all, comfort. These core values are evident in every appointment across our customizable array of services.
Our goal is to establish a benchmark for exceptional hair care for every human.
Website: www.morvanehairstudio-demo.com
instagram: @morvanehairstudio
address: 41872 Pelton Brook Rd, Larkmoor MI
phone: 248-316-8847

Industry/Entity Type

Hair Salon

Contact Information for Business Card

Stylist name, title, phone, instagram, website, address, (optional qr code)

Requirements
Should not have
• Does not need mission statement on the card.

```html
<!DOCTYPE html>
<html lang="en">
<head>
<meta charset="utf-8">
<title>Morvane Hair Studio — Business Card</title>
<link href="https://fonts.googleapis.com/css2?family=Arimo:wght@400;700&display=swap" rel="stylesheet">
<style>
  :root {
    --stage: #e9e9e9;
    --card-dark: #333333;
    --card-light: #ffffff;
    --gold: #93874a;
    --ink-light: #f2f2f2;
  }
  * { box-sizing: border-box; margin: 0; padding: 0; }
  html, body {
    width: 1200px; height: 802px; overflow: hidden;
    background: var(--stage);
    font-family: "Arimo", Arial, sans-serif;
  }
  .sheet {
    width: 1200px; height: 802px;
    display: flex; flex-direction: column; align-items: center; justify-content: center;
    gap: 56px;
  }
  .card {
    width: 560px; height: 320px;
    display: flex; overflow: hidden;
    box-shadow: 0 6px 18px rgba(0,0,0,.18);
  }
  .front__brand {
    width: 50%; background: var(--card-light);
    display: flex; align-items: center; justify-content: center;
  }
  .brand-mark {
    width: 190px; height: 190px; border: 3px solid var(--gold); border-radius: 50%;
    display: flex; align-items: center; justify-content: center; text-align: center;
    flex: none;
  }
  .brand-name {
    color: var(--gold); font-weight: 700; text-transform: uppercase;
    font-size: 19px; letter-spacing: 3px; line-height: 1.35;
  }
  .front__info {
    width: 50%; background: var(--card-dark);
    padding: 34px 28px 30px 20px;
    display: flex; flex-direction: column; justify-content: space-between; text-align: right;
  }
  .stylist__name { color: var(--gold); font-weight: 700; font-size: 19px; letter-spacing: .5px; text-transform: uppercase; }
  .stylist__title { color: var(--ink-light); font-size: 14px; margin-top: 3px; }
  .contact { list-style: none; display: flex; flex-direction: column; gap: 7px; }
  .contact__item {
    display: flex; justify-content: flex-end; align-items: center; gap: 7px;
    color: var(--ink-light); font-size: 13px; white-space: nowrap;
  }
  .contact__item--plain { padding-right: 19px; }
  .contact__icon { width: 12px; height: 12px; flex: none; }
  .back { background: var(--card-dark); padding: 0 40px; align-items: center; justify-content: space-between; }
  .services { list-style: none; display: flex; flex-direction: column; gap: 6px; }
  .services__item { color: var(--ink-light); font-size: 17px; display: flex; align-items: center; gap: 9px; }
  .services__item::before { content: ""; width: 7px; height: 7px; border-radius: 50%; background: var(--gold); }
  .back .brand-mark { width: 200px; height: 200px; }
</style>
</head>
<body>
<main class="sheet">
  <section class="card front">
    <div class="front__brand">
      <div class="brand-mark"><p class="brand-name">Morvane<br>Hair Studio</p></div>
    </div>
    <div class="front__info">
      <header class="stylist">
        <h1 class="stylist__name">Daniel Reyes</h1>
        <p class="stylist__title">Manager</p>
      </header>
      <ul class="contact">
        <li class="contact__item">248-316-8847
          <svg class="contact__icon" viewBox="0 0 24 24"><path fill="var(--gold)" d="M6.6 10.8a15 15 0 0 0 6.6 6.6l2.2-2.2c.3-.3.7-.4 1-.2 1.1.4 2.3.6 3.6.6.6 0 1 .4 1 1V20c0 .6-.4 1-1 1A17 17 0 0 1 3 4c0-.6.4-1 1-1h3.5c.6 0 1 .4 1 1 0 1.3.2 2.5.6 3.6.1.3 0 .7-.2 1z"/></svg></li>
        <li class="contact__item">@morvanehairstudio
          <svg class="contact__icon" viewBox="0 0 24 24"><circle cx="12" cy="12" r="10" fill="var(--gold)"/></svg></li>
        <li class="contact__item">www.morvanehairstudio-demo.com
          <svg class="contact__icon" viewBox="0 0 24 24" fill="none" stroke="var(--gold)" stroke-width="2"><circle cx="12" cy="12" r="10"/><path d="M2 12h20M12 2c3 3 3 17 0 20M12 2c-3 3-3 17 0 20"/></svg></li>
        <li class="contact__item">41872 Pelton Brook Rd
          <svg class="contact__icon" viewBox="0 0 24 24"><path fill="var(--gold)" d="M12 2a7 7 0 0 0-7 7c0 5 7 13 7 13s7-8 7-13a7 7 0 0 0-7-7zm0 9.5A2.5 2.5 0 1 1 12 6.5a2.5 2.5 0 0 1 0 5z"/></svg></li>
        <li class="contact__item contact__item--plain">Larkmoor MI</li>
      </ul>
    </div>
  </section>

  <section class="card back">
    <ul class="services">
      <li class="services__item">Custom Haircuts</li>
      <li class="services__item">Coloring</li>
      <li class="services__item">Extensions</li>
      <li class="services__item">And Barbering</li>
      <li class="services__item">Beard Grooming</li>
    </ul>
    <div class="brand-mark"><p class="brand-name">Morvane<br>Hair Studio</p></div>
  </section>
</main>
</body>
</html>
```